Design needed for Cover of Conference Brochure

We are a conference company that puts on several business conferences per year. We are putting together a new conference - the Clearpath Forum Week, and our audience is UX practitioners and specialists, product designers, UX designers, etc.
We need a brochure cover created. We are looking for fresh design ideas and are open to varying color schemes - please just keep in mind that this is a conference for business professionals, and fonts and colors should reflect this. Only restriction is that we do have a general cover format that we follow - i.e. which text goes where. (I've attached samples from our other events to reference.) We also generally have a central image to each brochure - feel free to submit a few versions with different images... we want something that accurately represents UX. However, if the design is compelling enough, image might not be completely necessary. We are relatively flexible - we just want something sharp!
- Must include BWKT logo (see placing on sample event covers)
- Must include footer - see sample covers
- Red text in word document are notes to you the designer - not actual text meant to appear on the cover
This cover is standard 8x11, and will be used for web only, not print. I have attached a word doc that includes all of the text that you will need for the cover. We will need final version in PDF, jpeg, and PSD. Please message me with any questions or clarification.

```html
<!DOCTYPE html>
<html lang="en">
<head>
<meta charset="utf-8">
<title>Clearpath Forum Week — Brochure Cover</title>
<link href="https://fonts.googleapis.com/css2?family=Arimo:ital,wght@0,400;0,700;1,700&family=Cabin+Condensed:wght@500;600&family=Titan+One&display=swap" rel="stylesheet">
<style>
  :root {
    --orange: #f05a1c;
    --orange-deep: #e8501a;
    --grey-text: #555b60;
    --grey-band: #e4e4e4;
    --grey-line: #d2d2d2;
    --paper: #ffffff;
    --paper-soft: #f3f3f3;
    --note: #fbf28a;
    --note-edge: #f2e66c;
    --tape: rgba(240, 228, 120, 0.85);
    --pill: #4d5054;
    --footer: #d9d9d9;
    --brand-blue: #1c8fd6;
    --ink: #3d3d3d;
  }
  * { margin: 0; padding: 0; box-sizing: border-box; }
  html, body { width: 873px; height: 1200px; overflow: hidden; background: var(--paper); }
  .cover {
    position: relative;
    width: 873px;
    height: 1200px;
    overflow: hidden;
    background: var(--paper);
    font-family: "Arimo", Arial, sans-serif;
  }

  /* Brand mark */
  .brand {
    position: absolute;
    top: 30px;
    right: 28px;
    display: flex;
    align-items: center;
    gap: 8px;
  }
  .brand-square { width: 22px; height: 22px; background: var(--brand-blue); }
  .brand-name { font-weight: 700; font-size: 26px; color: var(--brand-blue); letter-spacing: 1px; }

  /* Title */
  .title { position: absolute; left: 112px; top: 70px; color: var(--orange); font-weight: 700; }
  .title-first { position: absolute; left: 0; top: 0; font-size: 96px; line-height: 1; letter-spacing: -1px; }
  .title-middle { position: absolute; left: 4px; top: 104px; font-size: 38px; font-style: italic; line-height: 1; }
  .title-last { position: absolute; left: 128px; top: 84px; font-size: 96px; line-height: 1; letter-spacing: -1px; white-space: nowrap; }

  .tagline {
    position: absolute;
    left: 300px;
    top: 247px;
    font-size: 21px;
    color: var(--grey-text);
  }

  /* Grey band */
  .band {
    position: absolute;
    left: 0;
    top: 303px;
    width: 873px;
    height: 174px;
    background: linear-gradient(180deg, #e9e9e9, var(--grey-band));
    border-top: 1px solid var(--grey-line);
    border-bottom: 1px solid var(--grey-line);
  }

  /* Date badge */
  .date-badge {
    position: absolute;
    left: 568px;
    top: 298px;
    width: 198px;
    height: 198px;
    border-radius: 50%;
    background: var(--orange);
    color: #fff;
    font-weight: 700;
    font-size: 38px;
    line-height: 1.22;
    display: flex;
    align-items: center;
    justify-content: center;
    text-align: center;
    box-shadow: 0 3px 6px rgba(0,0,0,0.15);
  }

  /* Sticky note */
  .note {
    position: absolute;
    left: 70px;
    top: 350px;
    width: 290px;
    height: 280px;
    background: linear-gradient(160deg, #fdf79c, var(--note) 60%, var(--note-edge));
    transform: rotate(-3deg);
    box-shadow: 6px 14px 18px rgba(0,0,0,0.28);
  }
  .tape {
    position: absolute;
    width: 98px;
    height: 30px;
    background: var(--tape);
  }
  .tape-left { left: 52px; top: 318px; transform: rotate(22deg); }
  .tape-right { left: 272px; top: 340px; transform: rotate(-28deg); }
  .note-text {
    position: absolute;
    left: 108px;
    top: 418px;
    width: 260px;
    transform: rotate(7deg);
    transform-origin: left top;
    color: var(--ink);
    font-size: 25px;
    line-height: 1.95;
  }
  .note-text .save { color: var(--orange); font-weight: 700; font-size: 30px; }

  /* Venue */
  .venue {
    position: absolute;
    left: 421px;
    top: 598px;
    font-family: "Cabin Condensed", "Arial Narrow", sans-serif;
    font-weight: 600;
    font-size: 32px;
    line-height: 1.25;
  }
  .venue-name { color: var(--orange-deep); }
  .venue-city { color: var(--grey-text); }

  /* Highlights */
  .lower {
    position: absolute;
    left: 0;
    top: 752px;
    width: 873px;
    height: 318px;
    background: linear-gradient(180deg, var(--paper-soft), #fafafa);
  }
  .highlights {
    position: absolute;
    left: 98px;
    top: 811px;
    width: 682px;
    height: 197px;
    background: #fbfbfb;
    box-shadow: 0 8px 14px rgba(0,0,0,0.12);
    padding: 22px 24px 0 30px;
    list-style: none;
  }
  .highlights li {
    position: relative;
    padding-left: 26px;
    font-size: 16.5px;
    line-height: 30px;
    color: var(--grey-text);
  }
  .highlights li svg { position: absolute; left: 0; top: 8px; }

  /* Footer */
  .footer {
    position: absolute;
    left: 0;
    top: 1069px;
    width: 873px;
    height: 131px;
    background: var(--footer);
    border-top: 1px solid #c8c8c8;
  }
  .register {
    position: absolute;
    left: 30px;
    top: 1110px;
    font-family: "Titan One", "Arial Black", sans-serif;
    font-size: 40px;
    color: var(--orange);
    text-shadow: 2px 2px 0 #5a2a10;
    letter-spacing: 1px;
  }
  .contact-pill {
    position: absolute;
    left: 397px;
    top: 1106px;
    width: 490px;
    height: 61px;
    border-radius: 31px 0 0 31px;
    background: var(--pill);
    color: #fff;
    font-size: 15px;
    display: flex;
    align-items: center;
    padding-left: 34px;
  }
  .contact-divider { width: 1px; height: 36px; background: #c9c9c9; margin: 0 22px; }
</style>
</head>
<body>
<main class="cover">
  <div class="brand">
    <span class="brand-square"></span>
    <span class="brand-name">BWKT</span>
  </div>

  <h1 class="title">
    <span class="title-first">Clearpath</span>
    <span class="title-middle">Forum</span>
    <span class="title-last" style="left:420px;top:84px;">Week</span>
  </h1>

  <p class="tagline">Design Compelling Experiences through Successful UX</p>

  <div class="band"></div>

  <div class="date-badge">June<br>10-12/<br>2014</div>

  <div class="note"></div>
  <div class="tape tape-left"></div>
  <div class="tape tape-right"></div>
  <p class="note-text">Register by<br>March 7th, 2014<br>&amp; <span class="save">Save $400!</span></p>

  <p class="venue">
    <span class="venue-name">Harborline Commons Club &amp;</span><br>
    <span class="venue-city">Hotel San Francisco, CA</span>
  </p>

  <div class="lower"></div>
  <ul class="highlights">
    <li><svg width="14" height="14" viewBox="0 0 14 14"><path d="M5 0h4v5h5v4H9v5H5V9H0V5h5z" fill="#f05a1c"/></svg>Case Studies from Leading Brands on Executing an Effective UX Strategy</li>
    <li><svg width="14" height="14" viewBox="0 0 14 14"><path d="M5 0h4v5h5v4H9v5H5V9H0V5h5z" fill="#f05a1c"/></svg>Learn How UX-Driven Innovation Can Change Your Business</li>
    <li><svg width="14" height="14" viewBox="0 0 14 14"><path d="M5 0h4v5h5v4H9v5H5V9H0V5h5z" fill="#f05a1c"/></svg>Build a Successful UX Team that Operates Strategically</li>
    <li><svg width="14" height="14" viewBox="0 0 14 14"><path d="M5 0h4v5h5v4H9v5H5V9H0V5h5z" fill="#f05a1c"/></svg>Insights into UX Research, User Behavior, Usability Testing, Lean UX, and More</li>
  </ul>

  <div class="footer"></div>
  <p class="register">Register Today !</p>
  <div class="contact-pill">
    <span>http://www.clearpathforumweek.com</span>
    <span class="contact-divider"></span>
    <span>888.555.0142</span>
  </div>
</main>
</body>
</html>
```